Heron Freightways LLC needs a web desigh ASAP!

We need a fully functioning web site for our trucking company!
we currently have our domain and logo.
Attached you will find our logo files and word documents with info we would like to include in our web page. (Navigation Tabs and dropdown menu)
Our domain is heronfreightways.net (from webnestly)
Our Chatterbook page is Heron Freightways LLC. You can find pictures and a little bit about our company.
our original logo is the one with bull on the left side.
Our trucking company is based in south Texas, but travel within the USA and Canada.

Target Market(s)

Logistic
Refrigerated Fleet Clients
Transportation
Trucking companies

Industry/Entity Type

Trucking Company

Coding

Coded - Design and coding required

Number of Pages Required

1 page

Font styles to use
Sans Serif

Colors
f04a51
3277b5
ffffff

Requirements
Must have
• our main email contact is Info@heronfreightways.net
• we would like see the colors of our logo. it would be nice to have a truck with our logo in the background.
• We need a web site that we can manage on our own easily.
Nice to have
• roads, highways
• get a quote module
• our inspirational web pages are:
• www.marwickhaulage.com
• www.dorvelcargo.com
• we are open to use stock photos

```html
<!DOCTYPE html>
<html lang="en">
<head>
<meta charset="utf-8">
<title>Heron Freightways LLC</title>
<link rel="stylesheet" href="https://fonts.googleapis.com/css2?family=Open+Sans:wght@400;600;700;800&display=swap">
<style>
:root{
  --red:#f04a51;
  --red-dark:#d93c43;
  --blue:#3277b5;
  --blue-dark:#245a8c;
  --white:#ffffff;
  --ink:#333333;
  --muted:#777777;
  --charcoal:#2b2b2b;
}
*{box-sizing:border-box;margin:0;padding:0}
html,body{width:1200px;height:3913px;overflow:hidden}
body{font-family:"Open Sans",Arial,sans-serif;color:var(--ink);background:var(--white);position:relative}
.abs{position:absolute}

/* Hero */
.hero{position:absolute;left:0;top:0;width:1200px;height:660px;
  background:linear-gradient(180deg,#aeb6bf 0%,#d9dde1 30%,#c5c9cc 55%,#7d8288 80%,#5a5d60 100%)}
.nav{position:absolute;left:86px;top:21px;width:1036px;height:94px;background:var(--white);
  display:flex;align-items:center;justify-content:space-between;padding:0 26px 0 34px;box-shadow:0 2px 6px rgba(0,0,0,.15)}
.brand{display:flex;align-items:center;gap:10px;font-weight:800;font-size:22px;color:var(--red)}
.brand-dot{width:16px;height:16px;background:var(--red)}
.menu{display:flex;gap:26px;list-style:none;font-size:12.5px;font-weight:700;color:var(--ink)}
.menu li.active{color:var(--red);border-bottom:2px solid var(--red);padding-bottom:6px}
.hero-box{position:absolute;left:326px;top:248px;width:548px;height:248px;background:rgba(20,20,20,.75);
  border:2px solid rgba(255,255,255,.85);text-align:center;color:var(--white);padding-top:24px}
.hero-box h1{font-size:60px;font-weight:600;line-height:70px;letter-spacing:.5px}
.hero-box .rule{width:470px;height:1px;background:rgba(255,255,255,.8);margin:14px auto 12px}
.hero-box p{font-size:18px;font-weight:400}
.arrow{position:absolute;top:340px;width:62px;height:62px}

/* About */
.about-rule{left:89px;top:749px;width:70px;height:3px;background:var(--red)}
.about-title{left:89px;top:756px;font-size:27px;font-weight:600;color:var(--red)}
.about-text{left:89px;top:808px;width:620px;font-size:14px;line-height:24px;color:var(--muted)}
.about-text p{margin-bottom:22px}
.btn-small{left:89px;top:1002px;width:94px;height:29px;background:var(--blue);color:var(--white);
  font-size:10px;font-weight:700;display:flex;align-items:center;justify-content:center}
.about-photo{left:754px;top:814px;width:355px;height:219px;background:linear-gradient(160deg,#4d5866,#2a323c 70%,#3a3a30)}

/* Services */
.services{position:absolute;left:0;top:1109px;width:1200px;height:1518px;background:var(--blue)}
.svc-rule{left:89px;top:1181px;width:82px;height:3px;background:var(--white)}
.svc-title{left:89px;top:1190px;font-size:27px;font-weight:600;color:var(--white)}
.svc-lead{left:89px;top:1244px;width:960px;font-size:16px;line-height:24px;color:var(--white)}
.card{position:absolute;width:313px;height:337px;background:var(--white);border:3px solid #e9edf2}
.card.active{border-color:var(--red)}
.card-photo{height:200px;background:linear-gradient(180deg,#8fb4dc 0%,#c7d9ea 45%,#9a9a84 60%,#5b5d58 100%)}
.card.active .card-photo{background:linear-gradient(160deg,#3c4550,#20262d)}
.card h3{font-size:18px;font-weight:600;color:var(--ink);margin:16px 0 8px 14px}
.card.active h3{color:var(--red)}
.card p{font-size:11.5px;line-height:18px;color:var(--muted);margin:0 14px}
.card p b{color:var(--blue)}
.btn-outline{left:480px;top:2499px;width:240px;height:68px;border:3px solid rgba(255,255,255,.7);
  background:var(--blue-dark);color:var(--white);font-size:20px;font-weight:600;display:flex;align-items:center;justify-content:center}

/* Quote band */
.quote{position:absolute;left:0;top:2627px;width:1200px;height:120px;background:var(--red)}
.quote p{position:absolute;left:89px;top:46px;font-size:17px;color:var(--white)}
.quote .btn-quote{position:absolute;left:856px;top:29px;width:255px;height:62px;border:3px solid var(--white);
  color:var(--white);font-size:23px;font-weight:600;display:flex;align-items:center;justify-content:center}

/* Stats */
.stats{position:absolute;left:0;top:2747px;width:1200px;height:305px;background:linear-gradient(100deg,#1d1d1d,#3a3a3a 55%,#262626)}
.stat{position:absolute;top:62px;color:var(--white)}
.stat .num{font-size:36px;font-weight:400}
.stat .bar{width:190px;height:3px;background:var(--white);margin:8px 0 26px}
.stat .label{font-size:17px;line-height:28px;text-transform:uppercase}

/* Contact */
.map{position:absolute;left:0;top:3052px;width:1200px;height:543px;background:linear-gradient(90deg,#5e5e5e 0%,#6a6a6a 50%,#d9d9d9 50%,#c8c8c8 100%)}
.contact{position:absolute;left:128px;top:3120px;width:430px;color:var(--white)}
.contact h2{font-size:19px;font-weight:700}
.contact .rule{position:absolute;left:0;top:-10px;width:60px;height:3px;background:var(--white)}
.contact .sub{font-size:12px;margin-top:2px}
.field{position:absolute;background:var(--white);color:#999;font-size:12px;padding:12px 10px}
.submit{position:absolute;left:0;top:245px;width:430px;height:45px;background:var(--red);color:var(--white);
  font-size:16px;font-weight:700;display:flex;align-items:center;justify-content:center}
.info{position:absolute;font-size:11px;line-height:15px;display:flex;gap:8px}

/* Footer */
.footer{position:absolute;left:0;top:3595px;width:1200px;height:274px;background:var(--red);color:var(--white)}
.footer .brand{position:absolute;left:89px;top:122px;color:var(--white);font-size:22px}
.footer .brand-dot{background:var(--white)}
.links{position:absolute;top:55px;list-style:none;font-size:11px;line-height:24px}
.links li::before{content:"";display:inline-block;width:9px;height:9px;background:var(--white);margin-right:12px}
.person{position:absolute;left:856px;font-size:11px;line-height:15px}
.person b{font-size:12.5px;font-weight:700;display:block}
.divider{position:absolute;left:856px;top:112px;width:255px;height:1px;background:rgba(255,255,255,.7)}
.bottom{position:absolute;left:0;top:3869px;width:1200px;height:44px;background:var(--red-dark);color:var(--white);
  font-size:10px;display:flex;align-items:center;justify-content:space-between;padding:0 40px 0 89px}
.follow{display:flex;align-items:center;gap:12px}
.follow span.circle{width:24px;height:24px;border-radius:50%;background:var(--white)}
</style>
</head>
<body>

<section class="hero" role="img" aria-label="Row of white freight trucks parked at a depot under a grey sky">
</section>
<nav class="nav">
  <div class="brand"><span class="brand-dot"></span>Heron Freightways</div>
  <ul class="menu">
    <li class="active">HOME</li><li>ABOUT US</li><li>WHAT WE DO</li><li>SERVICES</li><li>WHY CHOOSE US</li><li>CAREERS</li><li>CONTACT US</li>
  </ul>
</nav>
<div class="hero-box">
  <h1>FRIEGHT SERVICE<br>YOU CAN TRUST</h1>
  <div class="rule"></div>
  <p>ROAD, AIR, TRAIN OR OVERSEAS. WE GOT IT COVERED!</p>
</div>
<svg class="arrow" style="left:89px" viewBox="0 0 62 62"><circle cx="31" cy="31" r="29" fill="none" stroke="#111" stroke-width="2.5"/><path d="M35 20 L24 31 L35 42" fill="none" stroke="#111" stroke-width="3"/></svg>
<svg class="arrow" style="left:1046px" viewBox="0 0 62 62"><circle cx="31" cy="31" r="29" fill="none" stroke="#111" stroke-width="2.5"/><path d="M27 20 L38 31 L27 42" fill="none" stroke="#111" stroke-width="3"/></svg>

<section>
  <div class="abs about-rule"></div>
  <h2 class="abs about-title">A LITTLE ABOUT US</h2>
  <div class="abs about-text">
    <p>Our mission is to provide our clients with safe, consistent and quality transportation solutions.</p>
    <p>Our logistics team is committed to customer satisfaction, safety and trust. You can be sure your goods will be delivered on time and in the best condition.</p>
    <p>At Heron Freightways customer satisfaction it's our priority.</p>
  </div>
  <div class="abs btn-small">READ MORE</div>
  <div class="abs about-photo" role="img" aria-label="Company truck with the Heron Freightways name on its trailer, shown as a video still"></div>
</section>

<section class="services"></section>
<div class="abs svc-rule"></div>
<h2 class="abs svc-title">OUR SERVICES</h2>
<p class="abs svc-lead">veritatis et quasi architecto beatae vitae dicta sunt explicabo. Nemo enim ipsam voluptatem quia voluptas sit aspernatur aut odit aut fugit, sed quia consequuntur magni dolores eos qui</p>

<div class="card" style="left:89px;top:1346px"><div class="card-photo" role="img" aria-label="Truck on a desert highway"></div><h3>Freight Logistics</h3><p>Lorem ipsum dolor sit amet, consectetur adipiscing elit, sed do eiusmod tempor incididunt ut labore et dolore magna aliqua. Ut enim ad <b>Read More</b></p></div>
<div class="card active" style="left:443px;top:1346px"><div class="card-photo" role="img" aria-label="Company truck shown with a dark overlay"></div><h3>Dedicated Service</h3><p>Lorem ipsum dolor sit amet, consectetur adipiscing elit, sed do eiusmod tempor incididunt ut labore et dolore magna aliqua. Ut enim ad <b>Read More</b></p></div>
<div class="card" style="left:798px;top:1346px"><div class="card-photo" role="img" aria-label="Refrigerated trailer on an open road"></div><h3>Temperature Controlled</h3><p>Lorem ipsum dolor sit amet, consectetur adipiscing elit, sed do eiusmod tempor incididunt ut labore et dolore magna aliqua. Ut enim ad <b>Read More</b></p></div>

<div class="card" style="left:89px;top:1722px"><div class="card-photo" role="img" aria-label="Tanker truck under a blue sky"></div><h3>Dedicated Service</h3><p>Lorem ipsum dolor sit amet, consectetur adipiscing elit, sed do eiusmod tempor incididunt ut labore et dolore magna aliqua. Ut enim ad <b>Read More</b></p></div>
<div class="card" style="left:443px;top:1722px"><div class="card-photo" role="img" aria-label="Truck on a desert highway"></div><h3>Freight Logistics</h3><p>Lorem ipsum dolor sit amet, consectetur adipiscing elit, sed do eiusmod tempor incididunt ut labore et dolore magna aliqua. Ut enim ad <b>Read More</b></p></div>
<div class="card" style="left:798px;top:1722px"><div class="card-photo" role="img" aria-label="Refrigerated trailer on an open road"></div><h3>Temperature Controlled</h3><p>Lorem ipsum dolor sit amet, consectetur adipiscing elit, sed do eiusmod tempor incididunt ut labore et dolore magna aliqua. Ut enim ad <b>Read More</b></p></div>

<div class="card" style="left:89px;top:2097px"><div class="card-photo" role="img" aria-label="Truck on a desert highway"></div><h3>Freight Logistics</h3><p>Lorem ipsum dolor sit amet, consectetur adipiscing elit, sed do eiusmod tempor incididunt ut labore et dolore magna aliqua. Ut enim ad <b>Read More</b></p></div>
<div class="card" style="left:443px;top:2097px"><div class="card-photo" role="img" aria-label="Tanker truck under a blue sky"></div><h3>Dedicated Service</h3><p>Lorem ipsum dolor sit amet, consectetur adipiscing elit, sed do eiusmod tempor incididunt ut labore et dolore magna aliqua. Ut enim ad <b>Read More</b></p></div>
<div class="card" style="left:798px;top:2097px"><div class="card-photo" role="img" aria-label="Refrigerated trailer on an open road"></div><h3>Temperature Controlled</h3><p>Lorem ipsum dolor sit amet, consectetur adipiscing elit, sed do eiusmod tempor incididunt ut labore et dolore magna aliqua. Ut enim ad <b>Read More</b></p></div>

<div class="abs btn-outline">VIEW ALL SERVICES</div>

<section class="quote">
  <p>Facing any transportation problem? Consult with our experts confidently!</p>
  <div class="btn-quote">GET A QUOTE</div>
</section>

<section class="stats" role="img" aria-label="Aerial view of a highway at dusk, darkened">
</section>
<div class="stat" style="left:120px;top:2809px"><div class="num">35 YEARS</div><div class="bar"></div><div class="label">Of<br>transportation<br>experience</div></div>
<div class="stat" style="left:376px;top:2809px"><div class="num">22 +</div><div class="bar"></div><div class="label">Trsnaportation<br>facilities<br>provided</div></div>
<div class="stat" style="left:631px;top:2809px"><div class="num">6,959 +</div><div class="bar"></div><div class="label">Satisfied<br>customers<br>around globe</div></div>
<div class="stat" style="left:887px;top:2809px"><div class="num">22,258</div><div class="bar"></div><div class="label">Highly skilled<br>drivers in our<br>fleet</div></div>

<section class="map" role="img" aria-label="Greyscale street map of the service area with location pins"></section>
<form class="contact">
  <div class="rule"></div>
  <h2>CONTACT US</h2>
  <div class="sub">Questions? Comments? Need a Quote?</div>
  <div class="field" style="left:0;top:86px;width:210px;height:45px">Name</div>
  <div class="field" style="left:220px;top:86px;width:210px;height:45px">Email</div>
  <div class="field" style="left:0;top:141px;width:430px;height:94px">Message here...</div>
  <div class="submit">SUBMIT</div>
  <div class="info" style="left:0;top:322px">
    <svg width="14" height="18" viewBox="0 0 14 18"><path d="M7 0C3 0 0 3 0 7c0 5 7 11 7 11s7-6 7-11c0-4-3-7-7-7z" fill="#f04a51"/><circle cx="7" cy="7" r="2.5" fill="#fff"/></svg>
    <div><b>Main Office:</b><br>4120 N. Mesa Rd,<br>Alton, TX 78573</div>
  </div>
  <div class="info" style="left:220px;top:322px">
    <svg width="16" height="16" viewBox="0 0 16 16"><path d="M3 1l3 3-2 2c1 2 3 4 5 5l2-2 3 3-2 3C7 15 1 9 1 3z" fill="#f04a51"/></svg>
    <div><b>Toll Free Number</b><br>1-800-555-0142<br><br><b>Local Number</b><br>(956) 555-0187</div>
  </div>
  <div class="info" style="left:0;top:398px">
    <svg width="16" height="12" viewBox="0 0 16 12"><rect width="16" height="12" fill="#f04a51"/><path d="M0 0l8 6 8-6" fill="none" stroke="#fff" stroke-width="1.4"/></svg>
    <div>Info@heronfreightways.net</div>
  </div>
</form>

<footer class="footer">
  <div class="brand"><span class="brand-dot"></span>Heron Freightways</div>
  <ul class="links" style="left:386px">
    <li>CONTACT US</li><li>FAQ'S</li><li>CAREERS</li><li>OUR BRANCHES</li><li>CUSTOMER CARE</li><li>PARTNERS</li><li>COLLABORATIONS</li>
  </ul>
  <ul class="links" style="left:577px">
    <li>CONTACT US</li><li>FAQ'S</li><li>CAREERS</li><li>OUR BRANCHES</li>
  </ul>
  <div class="person" style="top:58px"><b>MARCUS T. ALBRIGHT</b>GENERAL MANAGER<br>marcus.albright@heronfreightways.net</div>
  <div class="divider"></div>
  <div class="person" style="top:132px"><b>RENATA SOLIS</b>OFFICE MANAGER/ACCOUNTING<br>renata.solis@heronfreightways.net</div>
</footer>
<div class="bottom">
  <span>© HERON FREIGHTWAYS LLC. ALL RIGHTS RESERVED</span>
  <span class="follow">FOLLOW US ON <span class="circle"></span></span>
</div>

</body>
</html>
```